Web Site

Target Market(s)

CEOs and International Sales & Marketing Directors of International Companies who wish to expand their business reach to Dubai and the Middle East and are looking for a local professional partner to work with.

Requirements
Must have
• Creativity is key. We don't want the normal standard boxes of text and boxes of pics. Be as creative as you like.
Nice to have
• (This is only a suggestion, we welcome your creativity)
- The center of all pages could be large rotating pictures which display professional corporate men/women working in an office, images of Dubai, the UAE, skyscrapers of business towers in Dubai, ..etc.
- Images should reflect Dubai and the Arab World as a modern, fast-paced, growing modern market - Not Traditional)
Should not have
• Not so colorful, the fewer colors you use, the better.
Not Crammed or Busy
Not Traditional but modern

```html
<!DOCTYPE html>
<html lang="en">
<head>
<meta charset="utf-8">
<title>Cedar Group</title>
<link href="https://fonts.googleapis.com/css2?family=Ubuntu:wght@400;500&family=Arimo:wght@400;700&display=swap" rel="stylesheet">
<style>
:root{
  --sky:#d8edf5;
  --red:#9b0a14;
  --red-dark:#6e0509;
  --red-text:#8a0a16;
  --ink:#2b2b2b;
  --grey-text:#777;
  --panel:#f2f2f2;
  --line:#d9d9d9;
  --green:#6cbf2a;
  --footer:#3a3a3a;
  --link-blue:#36a6c7;
}
*{margin:0;padding:0;box-sizing:border-box}
html,body{width:1119px;height:1200px;overflow:hidden}
body{position:relative;background:#f4f4f4;font-family:'Ubuntu',sans-serif;color:var(--ink)}
.abs{position:absolute}
.top-band{left:0;top:0;width:1119px;height:134px;background:linear-gradient(#d4ebf4,#e6f3f8)}
.util-tab{left:738px;top:0;width:306px;height:26px;background:#5b5b5b;clip-path:polygon(0 0,100% 0,100% 100%,28px 100%);display:flex;justify-content:flex-end;align-items:center;padding-right:16px;gap:0;font-size:12px;color:#eee}
.util-tab span{padding:0 10px}
.util-tab i{font-style:normal;color:#aaa}
.brand{left:100px;top:46px;display:flex;align-items:center;gap:10px;font-size:38px;font-weight:400;color:#3a3a3a;letter-spacing:1px}
.brand b{display:block;width:14px;height:14px;background:#3a3a3a;font-weight:400}
.call-line{left:588px;top:74px;font-size:16px;color:#444}
.call-line strong{font-size:22px;font-weight:500;color:#222}
.call-btn{left:921px;top:62px;width:128px;height:44px;border-radius:3px;background:linear-gradient(#8fd548,#5aac1e);color:#fff;font-size:19px;display:flex;align-items:center;justify-content:center;border:1px solid #4f9a1a}
.nav{left:0;top:134px;width:1119px;height:40px;background:linear-gradient(#b0101a,#8a0710);border-top:1px solid #c6202a;border-bottom:1px solid #6e0509}
.nav ul{list-style:none;position:absolute;left:79px;top:0;height:40px;display:flex}
.nav li{height:40px;line-height:40px;color:#fff;font-size:13.5px;padding:0 18px;border-right:1px solid rgba(255,255,255,.15)}
.nav li.active{background:#2a2a2a;border:1px solid #111;border-radius:3px 3px 0 0;padding:0 20px}
.nav li:last-child{border-right:0}
.hero{left:78px;top:188px;width:972px;height:392px}
.hero-caption{left:632px;top:278px;width:408px;height:168px;background:rgba(0,0,0,.72);color:#fff;padding:18px 8px}
.hero-caption h2{font-size:23px;font-weight:400;line-height:26px;margin-bottom:12px}
.hero-caption p{font-size:13px;line-height:16.5px}
.pager{left:487px;top:564px;width:148px;height:34px;background:#fff;border-radius:17px 17px 0 0;display:flex;justify-content:center;gap:4px;padding-top:8px}
.pager span{width:17px;height:17px;border-radius:50%;border:2px solid #888;background:#fff}
.pager span.on{background:var(--red);border-color:var(--red)}
.footer{left:0;top:1112px;width:1119px;height:88px;background:linear-gradient(#333,#444)}
.copyright{left:0;top:1166px;width:1119px;text-align:center;color:#fff;font-size:11.5px}
.main{left:85px;top:608px;width:961px;height:544px;background:#fff;border:1px solid #e2e2e2;border-radius:6px}
.contact{left:99px;top:630px;width:245px;height:314px;background:var(--panel);border:1px solid var(--line);border-radius:3px;padding:12px 8px}
.contact h3{font-size:19px;font-weight:400;color:#444;margin:0 0 14px 3px}
.contact label{display:block;font-family:'Arimo',sans-serif;font-size:11.5px;color:#333;margin:0 0 3px 0}
.contact .field{height:21px;background:#fff;border:1px solid #ddd;border-radius:3px;margin-bottom:17px}
.send{position:absolute;left:45px;top:254px;width:164px;height:44px;border-radius:3px;background:linear-gradient(#b01020,#7c0510);color:#fff;font-size:19px;display:flex;align-items:center;justify-content:center}
.recent{left:98px;top:960px;width:245px;height:171px;border:1px solid var(--line);border-radius:3px;padding:10px 10px}
.recent h3{font-size:19px;font-weight:400;color:#444;margin-bottom:8px}
.item{display:flex;gap:8px;font-family:'Arimo',sans-serif;font-size:10.5px;line-height:13px;color:#333;padding-bottom:8px}
.item+.item{border-top:1px solid var(--line);padding-top:8px}
.thumb-s{width:40px;height:40px;border:1px solid #ccc;padding:3px;flex:none}
.thumb-s div{width:100%;height:100%;background:linear-gradient(#b89a78,#5a4a3a)}
.item a{color:var(--link-blue)}
.showcase-title{left:384px;top:620px;font-size:16px;color:#444}
.showcase-title em{font-style:normal;color:var(--red-text)}
.showcase-title::before{content:"";display:inline-block;width:5px;height:5px;background:var(--red);transform:rotate(45deg);margin:0 6px 3px 2px}
.rule{left:384px;top:646px;width:633px;height:2px;background:#e3e3e3}
.prop{width:178px;height:108px;border:1px solid #ddd;padding:3px;background:#fff}
.prop div{width:100%;height:100%}
.cap{font-family:'Arimo',sans-serif;font-weight:700;font-size:11px;color:var(--red-text)}
.cap::before{content:"◆";font-size:6px;color:#8ab;margin-right:5px;vertical-align:2px}
.card{width:210px;height:140px;border:1px solid #ddd;padding:5px;background:#fff;border-radius:2px}
.card div{width:100%;height:100%}
.card-title{font-size:16px;color:#333}
.card-title em{font-style:normal;color:var(--red-text)}
.card-text{font-family:'Arimo',sans-serif;font-size:12px;line-height:15.5px;color:var(--grey-text);width:200px}
</style>
</head>
<body>
<div class="abs top-band"></div>
<nav class="abs util-tab"><span>Log-in</span><i>|</i><span>Brochures</span><i>|</i><span>Owners</span><i>|</i><span>FAQs</span></nav>
<div class="abs brand"><b></b>CEDAR GROUP</div>
<div class="abs call-line">Book online or call <strong>+971-4-555-0142</strong></div>
<div class="abs call-btn">Call Now:</div>

<nav class="abs nav"><ul>
<li class="active">HOME</li><li>ABOUT THE GROUP</li><li>CHAIRMAN'S MESSAGE</li><li>DIVISIONS</li><li>GROUP COMPANIE</li><li>EMPLOYMENT &amp; ASSOCIATION</li><li>CONTACT US</li>
</ul></nav>

<svg class="abs hero" viewBox="0 0 972 392" role="img" aria-label="Night skyline of city towers with light trails on a highway">
<defs><linearGradient id="heroSky" x1="0" y1="0" x2="0" y2="1">
<stop offset="0" stop-color="#6d6a72"/><stop offset=".35" stop-color="#3c302c"/><stop offset=".7" stop-color="#8a4a1e"/><stop offset="1" stop-color="#2a1e18"/></linearGradient></defs>
<path d="M0 0H972V358Q486 300 0 358Z" fill="url(#heroSky)"/>
</svg>
<div class="abs hero-caption">
<h2>DUBAI-BASED DIVERSIFIED GROUPS OF COMPANIES</h2>
<p>The Group has grown with Dubai, and while best known for Real Estate Investment, it is globally recognized through its involvement in the Legal Consultations, Media Production, General Trading, and Telecommunication Services sectors.</p>
</div>
<div class="abs pager"><span></span><span class="on"></span><span></span><span></span><span></span></div>

<div class="abs footer"></div>
<div class="abs copyright">COPYRIGHT - include a copyright statement © 2012 Cedar Group, Inc. | All rights reserved.</div>

<div class="abs main"></div>

<form class="abs contact">
<h3>Contact Form</h3>
<label>Name:</label><div class="field"></div>
<label>Mobile</label><div class="field"></div>
<label>Email:</label><div class="field"></div>
<label>Enquiry/Questions</label><div class="field"></div>
<div class="send">Send</div>
</form>

<aside class="abs recent">
<h3>Recently Added</h3>
<div class="item"><div class="thumb-s"><div role="img" aria-label="Living room interior"></div></div>
<div><a>Elm Court</a><br>Harbour End (3mls N),<br>North Vale<br>Sleeps:6 | Bedrooms:3</div></div>
<div class="item"><div class="thumb-s"><div role="img" aria-label="Bright room interior"></div></div>
<div><a>Ridgefield</a><br>Millbrook, Westdale<br>Sleeps:13 | Bedrooms:6</div></div>
</aside>

<div class="abs showcase-title">Property <em>Showcase</em></div>
<div class="abs rule"></div>

<svg class="abs" style="left:370px;top:706px" width="14" height="28" viewBox="0 0 14 28"><path d="M13 0V28L0 14Z" fill="#333"/></svg>
<svg class="abs" style="left:1015px;top:706px" width="14" height="28" viewBox="0 0 14 28"><path d="M1 0V28L14 14Z" fill="#333"/></svg>

<div class="abs prop" style="left:398px;top:666px"><div role="img" aria-label="Hotel pool hall with patterned columns" style="background:linear-gradient(#c9935a,#2aa0b8)"></div></div>
<div class="abs prop" style="left:610px;top:666px"><div role="img" aria-label="Illuminated resort building at night" style="background:linear-gradient(#1a1420,#c07a2a)"></div></div>
<div class="abs prop" style="left:823px;top:666px"><div role="img" aria-label="Hotel lobby lounge with seating" style="background:linear-gradient(#b9b3a6,#6a5030)"></div></div>
<div class="abs cap" style="left:401px;top:782px">Lorem Ipsum is</div>
<div class="abs cap" style="left:611px;top:782px">Lorem Ipsum is</div>
<div class="abs cap" style="left:824px;top:782px">Lorem Ipsum is</div>

<div class="abs card" style="left:374px;top:827px"><div role="img" aria-label="Two professionals reviewing documents outside a house" style="background:linear-gradient(#9fc0d8,#5b7a3a)"></div></div>
<div class="abs card" style="left:597px;top:827px"><div role="img" aria-label="Sound engineer at a mixing desk" style="background:linear-gradient(#8a8c88,#3a3a38)"></div></div>
<div class="abs card" style="left:820px;top:827px"><div role="img" aria-label="Pen pointing at a green bar chart" style="background:linear-gradient(#e8f4f8,#a9d84a)"></div></div>

<div class="abs card-title" style="left:385px;top:977px">Legal <em>Services</em></div>
<div class="abs card-title" style="left:602px;top:977px">Media <em>Production</em></div>
<div class="abs card-title" style="left:827px;top:977px">General <em>Trading</em></div>

<p class="abs card-text" style="left:384px;top:1007px">It includes legal consultations in all legal matters, drafting, reviewing and procurement of various types of contracts and agreements.</p>
<p class="abs card-text" style="left:601px;top:1007px">Lumen Studios is a Dubai based state of the art digital Media production facility; offering clients and advertising agencies a 'one stop shop' production facility in Audio/Video/Film.</p>
<p class="abs card-text" style="left:828px;top:1007px">Cedar General Trading is a leading trading company that specializes in trading in many different products ranging from food &amp; beverages, Fire &amp; Safety</p>
</body>
</html>
```